STATIONERY FOR OUR CLIENT

I have a client that is a major oilseed processor in Australia. They want a deluxe gorgeous version of their business card.
I am proposing we print the business cards in Pelbrix.com VARNO versions with the coloured edging, probably in black. Their business name needs to appear on both sides whether in logo or text.
The stationery needs to be layed up to look lifelike to impress the client. Ideally full stationery including letterhead, business card, with compliments, envelopes.
We want to impress our client.
*** The design needs to communicate - quality, premium, prestige, modern, expert, wealthy, abundant, sophisticated, established.
Designs need to be not too dark, not alot of black please. Clean, modern, sophisticated, upmarket, luxury brand.
I need 3 concepts to present to client and once approved, refined to then have print ready files - and working files just in case we have to make tweaks down the track.
We also need to create a one page style guide, that includes pms colour etc.
THIS IS AN URGENT JOB
Updates

Please design less with black more with clean white possibly light grey/beige as secondary colour if you are looking for contrast. I have added some examples of cards that look nice and might help with what the client is looking for. thank you and looking forward to seeing the designs

Please ensure all designs submitted have the correct contact details of our client which is in the brief. Also please do not have any black backgrounds - if any of your design do have black backgrounds, please amend. Thank you

Target Market(s)

business customers, investors, major distributors

Industry/Entity Type

Business

Font styles to use
Sans Serif

Requirements
Must have
• must have business name on both sides. designed to be printed with pelbrix.com using their VARNO business card print offering.
Should not have
• alot of black

```html
<!DOCTYPE html>
<html lang="en">
<head>
<meta charset="utf-8">
<title>KALO – Business Card</title>
<link rel="stylesheet" href="https://fonts.googleapis.com/css2?family=Lato:wght@300;400;700&display=swap">
<style>
  :root {
    --brand-green: #128a50;
    --brand-green-light: #5fae85;
    --brand-green-deep: #0d6b3d;
    --card-white: #ffffff;
    --back-panel: #f5f3ee;
    --stage: #e7e9e8;
    --divider: #d3ddd8;
    --ink-white: #ffffff;
  }
  * { box-sizing: border-box; margin: 0; padding: 0; }
  html, body {
    width: 1200px; height: 926px; overflow: hidden;
    background: var(--stage);
    font-family: "Lato", "Helvetica Neue", Arial, sans-serif;
  }
  .canvas {
    width: 1200px; height: 926px;
    display: flex; align-items: center; justify-content: center; gap: 44px;
  }
  .card {
    width: 540px; height: 310px; position: relative; overflow: hidden;
    box-shadow: 0 6px 18px rgba(0,0,0,.15);
  }

  /* Front */
  .card-front { background: var(--card-white); }
  .card-front .brand {
    position: absolute; left: 30px; top: 70px; width: 170px;
    color: var(--brand-green); text-align: center;
  }
  .brand-mark {
    width: 54px; height: 54px; border-radius: 50%;
    background: var(--brand-green); margin: 0 auto 14px;
  }
  .brand-name {
    font-weight: 400; font-size: 30px; letter-spacing: 14px;
    padding-left: 14px; line-height: 1;
  }
  .brand-tagline {
    font-weight: 400; font-size: 11.5px; margin-top: 6px; letter-spacing: .2px;
  }
  .divider {
    position: absolute; left: 222px; top: 26px; width: 1px; height: 200px;
    background: linear-gradient(var(--card-white), var(--divider) 30%, var(--divider) 70%, var(--card-white));
  }
  .person { position: absolute; left: 250px; top: 34px; color: var(--brand-green); }
  .person-name { font-size: 30px; font-weight: 300; line-height: 1; }
  .person-name strong { font-weight: 700; }
  .person-role {
    font-size: 11px; letter-spacing: 3.4px; color: var(--brand-green-light);
    margin-top: 6px; font-weight: 400;
  }
  .contact-list { list-style: none; margin-top: 22px; font-size: 15px; line-height: 21px; }
  .contact-list li { display: flex; }
  .contact-label { width: 26px; font-weight: 700; }
  .address-band {
    position: absolute; left: 0; right: 0; bottom: 0; height: 54px;
    background: var(--brand-green); color: var(--ink-white);
    font-size: 15px; letter-spacing: 2px;
    display: flex; align-items: center; padding-left: 26px;
  }

  /* Back */
  .card-back { background: var(--brand-green); padding: 24px; }
  .back-panel {
    width: 100%; height: 100%; background: var(--back-panel);
    display: flex; flex-direction: column; align-items: center; justify-content: center;
    color: var(--brand-green);
  }
  .back-panel .brand-mark { width: 64px; height: 64px; margin-bottom: 18px; }
  .back-panel .brand-name { font-size: 36px; letter-spacing: 18px; padding-left: 18px; }
  .back-panel .brand-tagline { font-size: 14px; }
</style>
</head>
<body>
<main class="canvas">
  <section class="card card-front" aria-label="Business card front">
    <div class="brand">
      <div class="brand-mark"></div>
      <div class="brand-name">KALO</div>
      <div class="brand-tagline">Kestrel Agri Oils &amp; BioEnergy</div>
    </div>
    <div class="divider"></div>
    <div class="person">
      <h1 class="person-name">R.K. <strong>Menon</strong></h1>
      <p class="person-role">MANAGING DIRECTOR</p>
      <ul class="contact-list">
        <li><span class="contact-label">M.</span>037420 5518</li>
        <li><span class="contact-label">T.</span>0417 628 903</li>
        <li><span class="contact-label">W.</span>kestreloils.com.au</li>
        <li><span class="contact-label">E.</span>hello@kestreloils.com.au</li>
        <li><span class="contact-label">F.</span>linkfeed.com/kestreloils</li>
      </ul>
    </div>
    <div class="address-band">Unit 7, 48 Larkfield Road, Elmvale VIC 3199</div>
  </section>

  <section class="card card-back" aria-label="Business card back">
    <div class="back-panel">
      <div class="brand-mark"></div>
      <div class="brand-name">KALO</div>
      <div class="brand-tagline">Kestrel Agri Oils &amp; BioEnergy</div>
    </div>
  </section>
</main>
</body>
</html>
```